Real Estate Listing Signs for standard Yard arms

I need real estate listing signs done, for the standard sized sign to be hung beneath a white yard arm. To match existing logo. Information to be included:
-Logo
-Business name
-Phone number
-Marden Fosk Tundra Circle & Marden Fosk realty logos (smaller print)

Colors to be Red and anywhere in the gray scale between black and white, or a combination of those.

Target Market(s)

Drive by visuals

Industry/Entity Type

Real Estate Agent

Colors

Designer to choose only greyscale colors for use in the design.

Requirements
Must have
• My Logo and business name in same/similar font to whats provided, the MF tundra circle logo (small on bottom or corner somewhere), My phone number, and a decent amount of red coloration on the sign.

```html
<!DOCTYPE html>
<html lang="en">
<head>
<meta charset="utf-8">
<title>Vastel Realty – Yard Sign</title>
<link href="https://fonts.googleapis.com/css2?family=Montserrat:wght@400;500;700&display=swap" rel="stylesheet">
<style>
  :root {
    --sign-red: #fe1020;
    --panel-gray: #4d4e50;
    --ink-white: #ffffff;
  }
  html, body {
    margin: 0;
    padding: 0;
    overflow: hidden;
    background: var(--sign-red);
  }
  .sign {
    position: relative;
    width: 1200px;
    height: 457px;
    background: var(--sign-red);
    font-family: "Montserrat", sans-serif;
    color: var(--ink-white);
    overflow: hidden;
  }
  .brand {
    position: absolute;
    left: 100px;
    top: 88px;
    width: 256px;
    text-align: center;
  }
  .brand-mark {
    display: block;
    width: 96px;
    height: 96px;
    margin: 18px auto 0;
    background: var(--ink-white);
  }
  .brand-name {
    margin: 30px 0 0;
    font-weight: 700;
    font-size: 51px;
    line-height: 47px;
    letter-spacing: 0.5px;
  }
  .agent-panel {
    position: absolute;
    left: 457px;
    top: 102px;
    right: 0;
    height: 253px;
    background: var(--panel-gray);
  }
  .agent-info {
    position: absolute;
    left: 78px;
    top: 40px;
    margin: 0;
    font-size: 49px;
    line-height: 56px;
    white-space: nowrap;
  }
  .agent-name {
    display: block;
    font-weight: 700;
  }
  .agent-phone,
  .agent-email {
    display: block;
    font-weight: 400;
  }
  .brokerage {
    position: absolute;
    left: 457px;
    top: 386px;
    margin: 0;
    font-weight: 500;
    font-size: 19px;
    line-height: 21px;
    text-transform: uppercase;
    letter-spacing: 0.3px;
  }
  .disclaimer {
    position: absolute;
    left: 835px;
    top: 400px;
    margin: 0;
    font-weight: 500;
    font-size: 14px;
    line-height: 19px;
    letter-spacing: 0.4px;
    text-transform: uppercase;
  }
</style>
</head>
<body>
  <main class="sign">
    <section class="brand">
      <span class="brand-mark" aria-hidden="true"></span>
      <h1 class="brand-name">Vastel<br>Realty</h1>
    </section>

    <section class="agent-panel">
      <p class="agent-info">
        <span class="agent-name">CORIN VASTEL</span>
        <span class="agent-phone">907-555-0148</span>
        <span class="agent-email">cvastel@mailbox.com</span>
      </p>
    </section>

    <p class="brokerage">MF Tundra Circle<br>Marden Fosk Realty</p>

    <p class="disclaimer">Each office independently<br>owned and operated</p>
  </main>
</body>
</html>
```